Tot Petal Product Label for Tear-Free Head-to-Toe Wash

Need a bottle label design for a new line of natural products targeting infants and children. Products are Pediatrician-developed and paraben-free, sulfate-free, fragrance-free, and cruelty-free. Design should be clean and have a high-end feel to it. Will need other product labels in Tot Petal line designed as well in upcoming projects.

Target Market(s)

Newborn to young elementary age children and their parents

Industry/Entity Type

Cosmetics/Beauty

Font styles to use
Other font styles liked:
• Brand fonts are Jost and Sonorous

Colors

Designer to choose colors to be used in the design.

Requirements
Must have
• Tot Petal logo, Pediatrician Developed logo, and a clean high-end feel to it. The label must fit the specialty bottle we will be using (label measurements and diagram will be provided) for the front and back of bottle only (NOT the side labels). It must include our list of ingredients (will provide once designer selected).
Nice to have
• Should stand out on the shelf of other baby products due to it's clean simplicity and high-end feel
Should not have
• too much of a "kiddie" feel to it (targeting the parents not the kids)

```html
<!DOCTYPE html>
<html lang="en">
<head>
<meta charset="utf-8">
<title>Tot Petal – Soothing Baby Lotion Label</title>
<link rel="stylesheet" href="https://fonts.googleapis.com/css2?family=Fredoka:wght@600&family=Jost:wght@400;500&display=swap">
<style>
  :root {
    --bg: #f6efe9;
    --label: #f7f0eb;
    --sage: #7a8580;
    --bronze: #94795a;
    --ink: #41464c;
    --badge: #3f444a;
    --shadow: rgba(60, 50, 45, 0.55);
  }
  html, body {
    margin: 0;
    padding: 0;
    width: 1200px;
    height: 1200px;
    overflow: hidden;
    background: var(--bg);
  }
  .canvas {
    position: relative;
    width: 1200px;
    height: 1200px;
    font-family: "Jost", sans-serif;
  }
  .label-shapes {
    position: absolute;
    inset: 0;
  }
  .panel {
    position: absolute;
    top: 245px;
    width: 484px;
    height: 697px;
    text-align: center;
  }
  .panel--front { left: 75px; }
  .panel--back { left: 640px; }
  .panel > * { position: absolute; left: 0; right: 0; margin: 0; }

  .brand-seal {
    top: 70px;
    left: 174px;
    right: auto;
    width: 116px;
    height: 116px;
    border: 1.5px solid var(--ink);
    border-radius: 50%;
    box-sizing: border-box;
    display: flex;
    align-items: center;
    justify-content: center;
    font-family: "Jost", sans-serif;
    font-weight: 500;
    font-size: 15px;
    letter-spacing: 2px;
    color: var(--ink);
  }
  .wordmark {
    font-family: "Fredoka", sans-serif;
    font-weight: 600;
    color: var(--sage);
    font-size: 98px;
    line-height: 94px;
    top: 182px;
    left: -20px;
    letter-spacing: 1px;
  }
  .tagline {
    top: 375px;
    left: -20px;
    color: var(--bronze);
    font-size: 23px;
    letter-spacing: 0.5px;
  }
  .product-name {
    top: 432px;
    left: -20px;
    color: var(--sage);
    font-size: 33px;
    line-height: 35px;
    letter-spacing: 2.5px;
  }
  .claims {
    top: 532px;
    left: -20px;
    color: var(--ink);
    font-size: 17px;
    line-height: 22px;
  }
  .volume {
    top: 637px;
    left: -20px;
    color: var(--sage);
    font-size: 26px;
    letter-spacing: 1px;
  }

  .section-title {
    top: 55px;
    color: var(--sage);
    font-size: 37px;
    letter-spacing: 2px;
  }
  .ingredients {
    top: 127px;
    left: 100px;
    right: 95px;
    color: var(--ink);
    font-size: 17.5px;
    line-height: 22.2px;
    letter-spacing: 0.6px;
  }
  .directions-title {
    top: 388px;
    color: var(--sage);
    font-size: 17.5px;
    letter-spacing: 0.5px;
  }
  .directions {
    top: 425px;
    color: var(--ink);
    font-size: 17.5px;
    line-height: 22px;
    letter-spacing: 0.6px;
  }
  .pediatric-badge {
    top: 500px;
    left: 180px;
    right: auto;
    width: 124px;
    height: 124px;
  }
  .footer-note {
    top: 650px;
    font-size: 15px;
    color: var(--ink);
    right: auto;
  }
  .footer-note--left { left: 86px; }
  .footer-note--right { left: 286px; }
</style>
</head>
<body>
<main class="canvas">
  <svg class="label-shapes" width="1200" height="1200" viewBox="0 0 1200 1200" aria-hidden="true">
    <defs>
      <path id="label-outline" d="M0,100 C0,45 35,32 62,26 Q242,-22 422,26 C449,32 484,45 484,100 L484,667 Q484,697 454,697 L30,697 Q0,697 0,667 Z"/>
      <filter id="label-shadow" x="-10%" y="-10%" width="130%" height="130%">
        <feDropShadow dx="6" dy="7" stdDeviation="4" flood-color="#3c322d" flood-opacity="0.55"/>
      </filter>
    </defs>
    <use href="#label-outline" x="75" y="245" fill="#f7f0eb" filter="url(#label-shadow)"/>
    <use href="#label-outline" x="640" y="245" fill="#f7f0eb" filter="url(#label-shadow)"/>
  </svg>

  <section class="panel panel--front">
    <div class="brand-seal">TOT PETAL</div>
    <h1 class="wordmark">TOT<br>PETAL</h1>
    <p class="tagline">PEDIATRICIAN DEVELOPED</p>
    <h2 class="product-name">SOOTHING<br>BABY LOTION</h2>
    <p class="claims">PARABEN-FREE - SULFATE-FREE<br>FRAGRANCE-FREE- CRUELTY-FREE</p>
    <p class="volume">8 FL OZ/237 ml</p>
  </section>

  <section class="panel panel--back">
    <h2 class="section-title">INGREDIENTS</h2>
    <p class="ingredients">Water, Glycerin, Cocos Nucrifera (Coconut) Oil, Cetearyl Alcohal, Ai-loe Barbadensis Leaf Juice, Eutyros-permum Parkl. (Shea) Butter, Glyce-tyl Stearate.-Caprylla/Capric Tri-glyceride, Simmondsia, Chinensis (Jojoba) Sead Oil, Sudlum Stearoyl Lactylate, Tocopherol, Xanthan Gum, Citric</p>
    <h3 class="directions-title">DIRECTIONS</h3>
    <p class="directions">Apply as needed to baby's skin.<br>For external use only.</p>
    <svg class="pediatric-badge" viewBox="0 0 124 124" role="img" aria-label="Pediatrician developed badge">
      <circle cx="62" cy="62" r="58" fill="none" stroke="#3f444a" stroke-width="4"/>
      <circle cx="62" cy="62" r="30" fill="#3f444a"/>
    </svg>
    <p class="footer-note footer-note--left">FRAGRANCE-FREE</p>
    <p class="footer-note footer-note--right">MADE IN JAPAN</p>
  </section>
</main>
</body>
</html>
```